Lionel Arbusto and Dwight Halvorsen Advertisement

We would like an ad that conveys understated elegance. We are a company that purchases estate jewelry watches and diamonds. We care to a wealthy, upscale clientele.

Target Market(s)

Wealthy upscale.

Industry/Entity Type

It Company

Requirements
Must have
• Elegant Design. Crisp Clean. Attached a doc of how the ad should be arranged.

```html
<!DOCTYPE html>
<html lang="en">
<head>
<meta charset="utf-8">
<title>Lionel Arbusto &amp; Dwight Halvorsen — Ready To Sell?</title>
<link href="https://fonts.googleapis.com/css2?family=EB+Garamond:wght@400;500&display=swap" rel="stylesheet">
<style>
  :root {
    --bg-top: #8c9bab;
    --bg-glow: #d3d9df;
    --bg-mid: #a7b3bf;
    --bg-bottom: #6b7c8e;
    --frame: #ffffff;
    --text: #ffffff;
    --panel: #ffffff;
    --panel-text: #2b2b2b;
    --stone-light: #f4f6f8;
    --stone-mid: #c9cfd6;
  }
  * { margin: 0; padding: 0; box-sizing: border-box; }
  html, body { width: 800px; height: 1200px; overflow: hidden; }
  body { font-family: "EB Garamond", Garamond, serif; color: var(--text); }

  .ad {
    position: relative;
    width: 800px;
    height: 1200px;
    background: linear-gradient(180deg,
      var(--bg-top) 0%,
      #a3afbc 35%,
      var(--bg-glow) 50%,
      var(--bg-mid) 62%,
      #8797a8 78%,
      var(--bg-bottom) 100%);
    text-align: center;
  }
  .ad__frame {
    position: absolute;
    inset: 33px;
    border: 2.5px solid var(--frame);
  }
  .ad__headline {
    position: absolute;
    top: 150px;
    left: 0; right: 0;
    font-size: 47px;
    font-weight: 400;
    letter-spacing: 0.3px;
  }
  .ad__stone {
    position: absolute;
    left: 248px;
    top: 296px;
    width: 304px;
    height: 376px;
    background: radial-gradient(ellipse at 50% 40%, var(--stone-light) 0%, var(--stone-mid) 55%, rgba(201,207,214,0) 75%);
  }
  .ad__brand {
    position: absolute;
    left: 253px;
    top: 688px;
    width: 309px;
    height: 124px;
    background: var(--panel);
    display: flex;
    align-items: center;
    justify-content: center;
  }
  .ad__brand-name {
    font-size: 17px;
    font-weight: 400;
    letter-spacing: 1.2px;
    color: var(--panel-text);
    text-transform: uppercase;
  }
  .ad__promise {
    position: absolute;
    top: 828px;
    left: 0; right: 0;
    font-size: 37px;
    line-height: 48px;
    font-weight: 400;
  }
  .ad__contact {
    position: absolute;
    top: 968px;
    left: 0; right: 0;
    font-size: 24px;
    line-height: 25.5px;
    font-style: normal;
  }
</style>
</head>
<body>
  <main class="ad">
    <div class="ad__frame"></div>

    <h1 class="ad__headline">Ready To Sell?</h1>

    <div class="ad__stone" role="img" aria-label="Photograph of a loose emerald-cut diamond with its reflection"></div>

    <div class="ad__brand">
      <span class="ad__brand-name">Lionel Arbusto &amp; Dwight Halvorsen</span>
    </div>

    <p class="ad__promise">Utmost Discretion<br>By Appointment</p>

    <address class="ad__contact">
      Via Serena<br>
      418-C Marlow Avenue<br>
      Coral Harbor, FL 33099<br>
      support@arbustohalvorsen.com<br>
      555.014.2290
    </address>
  </main>
</body>
</html>
```